Bref créative
Holloway & Daughters
Biz Card/Stationery
I need single sided standard sized Business Card [3.5" x 2"]
Spinnaker Font and what's in logo
Professional
Derek Fulton
Vice President, Operations
3172 W. Maple Boulevard
Indianapolis, IN
dfulton@hollowaydaughters.com
hollowaydaughters.com

```html
<!DOCTYPE html>
<html lang="en">
<head>
<meta charset="utf-8">
<title>Holloway &amp; Daughters — Business Card</title>
<link href="https://fonts.googleapis.com/css2?family=Spinnaker&display=swap" rel="stylesheet">
<style>
  :root {
    --gold: #c9962e;
    --gold-deep: #b8862a;
    --ink: #1b1b1b;
    --paper: #ffffff;
    --backdrop: #ececec;
    --on-gold: #fdf6e6;
  }
  * { margin: 0; padding: 0; box-sizing: border-box; }
  html, body {
    width: 1200px; height: 980px; overflow: hidden;
    background: var(--backdrop);
    font-family: "Spinnaker", sans-serif;
  }
  .sheet {
    position: relative; width: 1200px; height: 980px;
    display: flex; flex-direction: column; align-items: center; justify-content: center; gap: 60px;
  }
  .card {
    position: relative; width: 700px; height: 400px;
    border-radius: 18px; overflow: hidden;
    box-shadow: 0 6px 18px rgba(0,0,0,0.12);
  }

  /* Front */
  .card-front { background: var(--gold); }
  .card-front .wave { position: absolute; inset: 0; width: 100%; height: 100%; }
  .brand {
    position: absolute; top: 62px; left: 0; right: 0;
    display: flex; flex-direction: column; align-items: center;
  }
  .brand-row { display: flex; align-items: center; gap: 12px; }
  .brand-dot { width: 18px; height: 18px; border-radius: 50%; background: var(--ink); }
  .brand-name { color: var(--gold); font-size: 34px; letter-spacing: 1px; text-transform: uppercase; }
  .brand-tag { margin-top: 4px; color: var(--ink); font-size: 14px; letter-spacing: 5px; text-transform: uppercase; }

  .contact {
    position: absolute; left: 36px; bottom: 28px;
    list-style: none; color: var(--on-gold); font-size: 13px; line-height: 1.65;
  }
  .contact li { display: flex; align-items: center; gap: 9px; }
  .contact svg { width: 11px; height: 11px; fill: var(--on-gold); flex: none; }

  .person { position: absolute; right: 36px; bottom: 30px; text-align: right; color: var(--on-gold); }
  .person-name { font-size: 17px; letter-spacing: 1px; }
  .person-title { font-size: 12px; letter-spacing: 1px; margin-top: 2px; }

  /* Back */
  .card-back { background: var(--gold); }
  .back-web {
    position: absolute; top: 34px; left: 36px;
    color: var(--on-gold); font-size: 13px; letter-spacing: 5px; text-transform: uppercase;
  }
  .back-mark {
    position: absolute; right: 60px; bottom: 40px;
    width: 200px; height: 200px; border-radius: 50%;
    background: rgba(255,255,255,0.14);
  }
</style>
</head>
<body>
<main class="sheet">
  <section class="card card-front" aria-label="Business card front">
    <svg class="wave" viewBox="0 0 700 400" preserveAspectRatio="none" aria-hidden="true">
      <path d="M0 0 H700 V250 C600 282 470 245 360 214 C250 184 110 214 0 204 Z" fill="var(--ink)"/>
      <path d="M0 0 H700 V236 C600 268 470 231 360 200 C250 170 110 200 0 190 Z" fill="var(--paper)"/>
    </svg>
    <div class="brand">
      <div class="brand-row">
        <span class="brand-dot"></span>
        <span class="brand-name">Holloway &amp; Daughters</span>
      </div>
      <span class="brand-tag">Construction Group</span>
    </div>
    <ul class="contact">
      <li><svg viewBox="0 0 12 12"><path d="M6 0a4 4 0 0 0-4 4c0 3 4 8 4 8s4-5 4-8a4 4 0 0 0-4-4zm0 5.5A1.5 1.5 0 1 1 6 2.5a1.5 1.5 0 0 1 0 3z"/></svg>3172 W. Maple Boulevard</li>
      <li><svg viewBox="0 0 12 12"><circle cx="6" cy="6" r="0"/></svg>Indianapolis, IN</li>
      <li><svg viewBox="0 0 12 12"><path d="M2.5 0.5l2 2.5-1.2 1.3a7 7 0 0 0 4.4 4.4L9 7.5l2.5 2-1.3 2C5 11 1 7 0.5 1.8z"/></svg>(317) 555-0148</li>
      <li><svg viewBox="0 0 12 12"><path d="M0 2h12v8H0zM0.8 2.6L6 6.6l5.2-4v-.1H.8z" fill-rule="evenodd"/></svg>dfulton@hollowaydaughters.com</li>
      <li><svg viewBox="0 0 12 12"><path d="M6 0a6 6 0 1 0 0 12A6 6 0 0 0 6 0zm0 1.2a4.8 4.8 0 1 1 0 9.6A4.8 4.8 0 0 1 6 1.2zM1.5 5.4h9v1.2h-9z"/></svg>hollowaydaughters.com</li>
    </ul>
    <div class="person">
      <p class="person-name">Derek Fulton</p>
      <p class="person-title">Vice President, Operations</p>
    </div>
  </section>

  <section class="card card-back" aria-label="Business card back">
    <p class="back-web">www.hollowaydaughters.com</p>
    <div class="back-mark" role="img" aria-label="Faint brand mark decoration"></div>
  </section>
</main>
</body>
</html>
```